Side of Page Partnership-type Letterhead Design for Chiropractic Office

Side oriented letterhead with practice locations/demographics, physician names and company logo

Target Market(s)

Healthcare Professionals & Attorneys

Industry/Entity Type

Healthcare

Font styles to use
Other font styles liked:
• Font of Logo is Trajan Pro, but not a deal breaker if we try something else

Colors

Designer to choose colors to be used in the design.

Requirements
Must have
• All info from attached documents

```html
<!DOCTYPE html>
<html lang="en">
<head>
<meta charset="utf-8">
<title>Keystone Spine Care Letterhead</title>
<link rel="stylesheet" href="https://fonts.googleapis.com/css2?family=Arimo:wght@400;700&display=swap">
<style>
  :root {
    --backdrop: #2b2b2d;
    --paper: #ebebec;
    --sidebar: #1f1d1e;
    --sidebar-text: #f2f2f2;
    --body-text: #6d6d6f;
    --heading-text: #58585a;
    --logo-text: #3b3b3d;
    --accent-green: #5a9a35;
    --accent-orange: #e08a1e;
  }
  * { margin: 0; padding: 0; box-sizing: border-box; }
  html, body { width: 1200px; height: 1200px; overflow: hidden; }
  body {
    background: var(--backdrop);
    font-family: "Arimo", Arial, sans-serif;
    position: relative;
  }
  .letterhead {
    position: absolute;
    left: 200px; top: 34px;
    width: 800px; height: 1132px;
    background: var(--paper);
    overflow: hidden;
  }
  .sidebar {
    position: absolute; left: 0; top: 0;
    width: 210px; height: 1132px;
    background: var(--sidebar);
    color: var(--sidebar-text);
    font-size: 13.3px; line-height: 16px;
  }
  .sidebar-rule {
    position: absolute; left: 36px;
    width: 18px; height: 2px;
    background: var(--accent-green);
  }
  .physicians { position: absolute; left: 36px; top: 224px; list-style: none; }
  .location { position: absolute; left: 36px; }
  .contact-line { display: flex; align-items: center; gap: 4px; }
  .contact-line svg { width: 9px; height: 9px; flex: none; }
  .band-orange, .band-green {
    position: absolute; bottom: 0; height: 5px;
  }
  .band-orange { left: 0; width: 210px; background: var(--accent-orange); }
  .band-green { left: 212px; right: 0; background: var(--accent-green); }

  .letter-body {
    position: absolute; left: 265px; top: 0; width: 486px;
    color: var(--body-text); font-size: 13.3px; line-height: 18.7px;
  }
  .brand {
    position: absolute; top: 58px; left: 0;
    display: flex; align-items: center; gap: 10px;
  }
  .brand-name {
    color: var(--logo-text); font-size: 34px; line-height: 30px;
    font-weight: 400; letter-spacing: 0.5px;
  }
  .brand-name span { display: block; font-size: 25px; line-height: 26px; }
  .brand-mark { width: 28px; height: 28px; background: var(--accent-green); }
  .date { position: absolute; top: 195px; }
  .recipient { position: absolute; top: 251px; font-style: normal; }
  .recipient strong { color: var(--heading-text); }
  .salutation { position: absolute; top: 365px; }
  .paragraph { position: absolute; width: 486px; text-align: justify; }
  .p1 { top: 403px; } .p2 { top: 534px; } .p3 { top: 666px; }
  .closing { position: absolute; top: 798px; }
  .signature-area {
    position: absolute; top: 818px; left: -8px; width: 290px; height: 36px;
    background: linear-gradient(90deg, rgba(60,60,60,0.12), rgba(60,60,60,0.04));
  }
  .signer { position: absolute; top: 849px; }
  .signer strong { color: var(--heading-text); }
</style>
</head>
<body>
  <article class="letterhead">
    <aside class="sidebar">
      <div class="sidebar-rule" style="top:199px"></div>
      <ul class="physicians">
        <li>Daniel Orwell, DC, DACNB</li>
        <li>Nathan Orwell, DC</li>
        <li>Colin Fairbrook, DC</li>
        <li>Evan Thistlewood, DC</li>
        <li>Grant Mellows, DC</li>
        <li>Owen Rackliffe, DC</li>
        <li>Lucas Penhale, DC</li>
      </ul>
      <div class="sidebar-rule" style="top:418px"></div>

      <address class="location" style="top:441px;font-style:normal">
        <div>Brookhaven</div>
        <div>4120 N. Meridian St.</div>
        <div>Brookhaven, OH 43999</div>
        <div class="contact-line"><svg viewBox="0 0 10 10"><path d="M2 1l2 2-1 1.2c.6 1.3 1.5 2.2 2.8 2.8L7 6l2 2-1.3 1.3C4.5 9 1 5.5.7 2.3z" fill="var(--accent-orange)"/></svg>555-210-4400</div>
        <div class="contact-line"><svg viewBox="0 0 10 10"><rect x="2.5" y="0.5" width="5" height="3" fill="var(--accent-orange)"/><rect x="0.5" y="4" width="9" height="4" rx="1" fill="var(--accent-orange)"/><rect x="2.5" y="7" width="5" height="2.5" fill="var(--accent-orange)"/></svg>555-210-4401</div>
      </address>

      <address class="location" style="top:557px;font-style:normal">
        <div>Linden Falls</div>
        <div>218 N. Maple Ave.</div>
        <div>Linden Falls, OH 43998</div>
        <div class="contact-line"><svg viewBox="0 0 10 10"><path d="M2 1l2 2-1 1.2c.6 1.3 1.5 2.2 2.8 2.8L7 6l2 2-1.3 1.3C4.5 9 1 5.5.7 2.3z" fill="var(--accent-orange)"/></svg>555-320-5500</div>
        <div class="contact-line"><svg viewBox="0 0 10 10"><rect x="2.5" y="0.5" width="5" height="3" fill="var(--accent-orange)"/><rect x="0.5" y="4" width="9" height="4" rx="1" fill="var(--accent-orange)"/><rect x="2.5" y="7" width="5" height="2.5" fill="var(--accent-orange)"/></svg>555-320-5501</div>
      </address>

      <address class="location" style="top:669px;font-style:normal">
        <div>Riverton</div>
        <div>775 S. Cedar Rd</div>
        <div>Riverton, OH 43997</div>
        <div class="contact-line"><svg viewBox="0 0 10 10"><path d="M2 1l2 2-1 1.2c.6 1.3 1.5 2.2 2.8 2.8L7 6l2 2-1.3 1.3C4.5 9 1 5.5.7 2.3z" fill="var(--accent-orange)"/></svg>555-430-6600</div>
        <div class="contact-line"><svg viewBox="0 0 10 10"><rect x="2.5" y="0.5" width="5" height="3" fill="var(--accent-orange)"/><rect x="0.5" y="4" width="9" height="4" rx="1" fill="var(--accent-orange)"/><rect x="2.5" y="7" width="5" height="2.5" fill="var(--accent-orange)"/></svg>555-430-6601</div>
      </address>
    </aside>

    <section class="letter-body">
      <header class="brand">
        <div class="brand-name">KEYSTONE<span>SPINE CARE</span></div>
        <div class="brand-mark"></div>
      </header>

      <p class="date">January 1, 2050</p>
      <address class="recipient">
        <strong>Thomas Avery</strong><br>
        Managing Director<br>
        Co.Street, Building/Suite<br>
        City/State, Zip Code
      </address>
      <p class="salutation">Dear Thomas Avery,</p>

      <p class="paragraph p1">Lorem ipsum dolor sit amet, consectetuer adipiscing elit, sed diam nonummy nibh euismod tincidunt ut laoreet dolore magna aliquam erat volutpat. Ut wisi enim ad minim veniam, quis nostrud exerci tation ullamcorper suscipit lobortis nisl ut aliquip ex ea commodo consequat. Duis dolore te feugait nulla facilisi. Nam liber tempor cum soluta nobis eleifend option congue nihil imperdiet doming id quod mazim placerat facer possim assum.</p>
      <p class="paragraph p2">Consectetuer adipiscing elit, sed diam nonummy nibh euismod tincidunt ut laoreet dolore magna aliquam erat volutpat. Ut wisi enim ad minim veniam, quis nostrud exerci tation ullamcorper suscipit lobortis nisl ut aliquip ex ea commodo consequat. Consectetuer adipiscing elit, sed diam nonummy nibh euismod tincidunt ut laoreet dolore magna aliquam erat volutpat. Ut wisi enim ad minim veniam, quis nostrud exerci tation ullamcorper suscipit lobortis nisl ut aliquip ex ea commodo consequat.</p>
      <p class="paragraph p3">Duis dolore te feugait nulla facilisi. Nam liber tempor cum soluta nobis eleifend option congue nihil imperdiet doming id quod mazim placerat facer possim assum.Duis dolore te feugait nulla facilisi. Nam liber tempor cum soluta nobis eleifend option congue nihil imperdiet doming id quod mazim placerat facer possim assum.</p>

      <p class="closing">Sincerely Yours,</p>
      <div class="signature-area" role="img" aria-label="Handwritten signature of the managing director"></div>
      <p class="signer"><strong>Authorized Managing Director</strong><br>Your Company Name</p>
    </section>

    <div class="band-orange"></div>
    <div class="band-green"></div>
  </article>
</body>
</html>
```